Bright Harbor Property Institute

This must be done in word press and I will need about 7 tabs The home page, Information page, Schedule and Cost page which will link to a Email me form, a online registration a about us and location/contact tab Each tab will then open several other pages. The home page will describe different courses that we offer since all the schools are about the same you can get a good ideal by going to plomvex.example or keelwardhomeclasses.example and looking at their site I would like mine to be similar as the courses are exactly the same but I would like the site to be more modern I also need it to be in word press so I can change it and update the dates as they change I have attached he logo below

Target Market(s)

people interested in getting into real estate and those who need continuing education

Coding

Number of Pages Required

Font styles to use
Sans Serif

Colors
3276b5

Requirements
Must have
• A page to schedule classes, a tab so the college I am partnering with can link the online courses to the back side, a page that describes the type of classes I offer

```html
<!DOCTYPE html>
<html lang="en">
<head>
<meta charset="utf-8">
<title>Bright Harbor Property Institute</title>
<link href="https://fonts.googleapis.com/css2?family=Poppins:wght@400;500;600;700&display=swap" rel="stylesheet">
<style>
:root{
  --brand:#3276b5;
  --ink:#333a40;
  --text:#4a4f55;
  --muted:#777d83;
  --line:#d8dce0;
  --white:#ffffff;
  --page:#ffffff;
}
*{margin:0;padding:0;box-sizing:border-box}
html,body{width:1200px;height:2735px;overflow:hidden;background:var(--page)}
body{position:relative;font-family:"Poppins",sans-serif;color:var(--text)}
.abs{position:absolute}
a{text-decoration:none;color:inherit}

.top-nav{left:0;top:0;width:1200px;height:42px;background:var(--brand);display:flex;justify-content:space-between;align-items:center;padding:0 140px 0 143px}
.top-nav a,.footer-nav a{color:var(--white);font-size:12.5px;font-weight:500;letter-spacing:.3px;text-transform:uppercase}

.masthead{left:0;top:42px;width:1200px;height:117px}
.brand-mark{display:flex;align-items:center;gap:10px}
.brand-mark .dot{width:34px;height:34px;border-radius:50%;background:var(--brand)}
.brand-mark .name{font-size:21px;font-weight:600;color:var(--brand);line-height:1.1}
.masthead .brand-mark{position:absolute;left:143px;top:34px}
.contact-item{position:absolute;top:34px;display:flex;align-items:center;gap:10px}
.contact-item .label{color:var(--brand);font-weight:600;font-size:15px;line-height:1.1}
.contact-item .value{color:var(--ink);font-size:17px;line-height:1.3}
.contact-item .sep{width:1px;height:46px;background:var(--line)}

.hero{left:0;top:159px;width:1200px;height:461px;background:linear-gradient(180deg,#d9dadb 0%,#b9aea4 40%,#7d6e62 75%,#4b4845 100%)}
.hero-title{left:0;top:538px;width:1200px;text-align:center;color:var(--white);font-size:23px;font-weight:500;line-height:34px;text-shadow:0 1px 3px rgba(0,0,0,.4)}

.feature{top:688px;width:290px;text-align:center}
.feature svg{display:block;margin:0 auto}
.feature h3{font-size:19px;font-weight:600;color:var(--ink);margin-top:8px}
.feature p{font-size:12.5px;line-height:21.7px;color:var(--muted);margin-top:6px}
.feature .more{display:inline-flex;align-items:center;gap:6px;color:var(--brand);font-size:12.5px;font-weight:500;margin-top:8px}

.about-copy{left:143px;top:1090px;width:425px}
.eyebrow{font-size:14px;font-weight:600;color:var(--ink)}
.about-copy h2{font-size:29px;font-weight:600;color:var(--brand);line-height:40px;margin-top:2px}
.about-copy h2 span{display:block;color:var(--ink);font-weight:500;letter-spacing:.5px}
.about-copy h4{font-size:14px;font-weight:600;color:var(--brand);letter-spacing:.5px;margin:26px 0 6px -2px}
.about-copy p{font-size:13.2px;line-height:22.8px;color:var(--ink);text-align:justify}
.photo-class{left:605px;top:1079px;width:388px;height:423px;background:linear-gradient(160deg,#cfc8b8,#8b8676 55%,#4f4b44)}
.photo-laptop{left:783px;top:1265px;width:279px;height:323px;background:var(--white);padding:7px}
.photo-laptop div{width:100%;height:100%;background:linear-gradient(160deg,#a9c2de,#5f8fc2 55%,#3b6a9c)}

.city{left:0;top:2078px;width:1200px;height:353px;background:linear-gradient(180deg,#8a96a3 0%,#6f7a80 45%,#555c5d 100%)}
.inquiry{left:140px;top:1760px;width:918px;height:358px;background:var(--white);box-shadow:0 0 8px rgba(0,0,0,.12);text-align:center}
.inquiry h2{font-size:30px;font-weight:600;color:var(--ink);margin-top:55px;letter-spacing:.5px}
.inquiry h2 b{color:var(--brand);font-weight:600}
.inquiry .lead{font-size:14.5px;color:var(--ink);margin-top:2px}
.fields{display:grid;grid-template-columns:repeat(3,254px);gap:15px 14px;margin:28px 0 0 64px;text-align:left}
.field{height:35px;border:1px solid var(--line);font-size:12px;color:#8d9297;padding:9px 14px}
.submit{display:inline-block;margin-top:35px;width:106px;height:32px;line-height:32px;background:var(--brand);color:var(--white);font-size:13px;font-weight:500}
.ready{left:0;top:2200px;width:1200px;text-align:center;color:var(--white)}
.ready h2{font-size:47px;font-weight:600;letter-spacing:1px}
.ready a{display:inline-block;margin-top:20px;width:168px;height:55px;line-height:55px;background:var(--brand);font-size:18px;font-weight:500;letter-spacing:.5px}

.footer{left:0;top:2431px;width:1200px;height:304px;background:var(--brand)}
.footer .brand-mark{position:absolute;left:0;width:1200px;justify-content:center;top:85px}
.footer .brand-mark .dot{background:var(--white)}
.footer .brand-mark .name{color:var(--white);font-size:24px}
.social{position:absolute;left:0;top:168px;width:1200px;display:flex;justify-content:center;gap:22px}
.social span{width:16px;height:16px;border-radius:50%;background:var(--white)}
.footer-nav{position:absolute;left:174px;top:220px;width:852px;display:flex;justify-content:space-between}
.copyright{position:absolute;left:0;top:264px;width:1200px;text-align:center;color:var(--white);font-size:12px}
</style>
</head>
<body>

<nav class="top-nav abs">
  <a href="#">Home</a><a href="#">About Us</a><a href="#">Schedule and Cost</a><a href="#">Registration</a><a href="#">Online Courses</a><a href="#">Our Advantage</a><a href="#">Contact Us</a>
</nav>

<header class="masthead abs">
  <div class="brand-mark"><span class="dot"></span><span class="name">Bright Harbor<br>Property Institute</span></div>
  <div class="contact-item" style="left:672px">
    <svg width="30" height="34" viewBox="0 0 30 34" fill="none" stroke="#3276b5" stroke-width="2"><path d="M8 3c-3 2-5 5-4 10 2 8 8 15 15 18 3 1 5 0 7-2l-5-6-4 2c-3-2-6-6-7-10l3-3z"/></svg>
    <span class="sep"></span>
    <div><div class="label">Call Us:</div><div class="value">1-010-555-0147</div></div>
  </div>
  <div class="contact-item" style="left:867px">
    <svg width="32" height="30" viewBox="0 0 32 30" fill="none" stroke="#3276b5" stroke-width="2"><path d="M2 9l28-7-4 26L2 9zM2 9l12 7 16-14M14 16l2 9"/></svg>
    <span class="sep"></span>
    <div><div class="label">Mail Us:</div><div class="value">info@brightharbor.example</div></div>
  </div>
</header>

<div class="hero abs" role="img" aria-label="Photo of an instructor teaching a classroom of students"></div>
<h1 class="hero-title abs">We Provide Classes For People To Fulfill License Requirements &amp; Continuing<br>Education Classes &nbsp;For Licensed Real Estate Agents</h1>

<section class="feature abs" style="left:133px">
  <svg width="72" height="72" viewBox="0 0 72 72" fill="none" stroke="#3276b5" stroke-width="2"><rect x="22" y="4" width="46" height="34"/><circle cx="44" cy="20" r="8"/><path d="M44 12v8h8M28 30h12"/><circle cx="12" cy="22" r="5"/><path d="M4 70V36h16l10-8M8 70V52M16 70V52"/><circle cx="38" cy="52" r="5"/><circle cx="56" cy="52" r="5"/><path d="M28 70c0-8 20-8 20 0M46 70c0-8 20-8 20 0"/></svg>
  <h3>Search Live Classes</h3>
  <p>Lorem ipsum dolor sit amet, consectetuer adipiscing elit, sed diam nonummy nibh euismod tincidunt ut laoreet dolore magna aliquam erat volutpat. Ut wisi enim</p>
  <a class="more" href="#">Learn More <svg width="14" height="10" viewBox="0 0 14 10" fill="none" stroke="#3276b5" stroke-width="1.6"><path d="M0 5h12M8 1l4 4-4 4"/></svg></a>
</section>
<section class="feature abs" style="left:455px">
  <svg width="72" height="72" viewBox="0 0 72 72" fill="none" stroke="#3276b5" stroke-width="2"><rect x="2" y="2" width="68" height="44" rx="3"/><path d="M10 2v44M62 2v44M20 12l8 5-8 5zM34 14h20M34 22h20M20 32h34"/><circle cx="10" cy="56" r="4"/><circle cx="28" cy="56" r="4"/><circle cx="46" cy="56" r="4"/><circle cx="62" cy="56" r="4"/><path d="M3 70c0-6 14-6 14 0M21 70c0-6 14-6 14 0M39 70c0-6 14-6 14 0M55 70c0-6 14-6 14 0"/></svg>
  <h3>Online Classes</h3>
  <p>Lorem ipsum dolor sit amet, consectetuer adipiscing elit, sed diam nonummy nibh euismod tincidunt ut laoreet dolore magna aliquam erat volutpat. Ut wisi enim</p>
  <a class="more" href="#">Learn More <svg width="14" height="10" viewBox="0 0 14 10" fill="none" stroke="#3276b5" stroke-width="1.6"><path d="M0 5h12M8 1l4 4-4 4"/></svg></a>
</section>
<section class="feature abs" style="left:775px">
  <svg width="72" height="72" viewBox="0 0 72 72" fill="none" stroke="#3276b5" stroke-width="2"><rect x="2" y="2" width="62" height="42"/><rect x="10" y="10" width="20" height="16"/><path d="M36 12h22M36 20h18M10 34h40M2 50h50M20 50v12h24M56 40c6 0 10 4 10 10v12c0 6-4 10-10 10s-10-4-10-10V50c0-6 4-10 10-10zM56 40v12"/></svg>
  <h3>Registration</h3>
  <p>Lorem ipsum dolor sit amet, consectetuer adipiscing elit, sed diam nonummy nibh euismod tincidunt ut laoreet dolore magna aliquam erat volutpat. Ut wisi enim</p>
  <a class="more" href="#">Learn More <svg width="14" height="10" viewBox="0 0 14 10" fill="none" stroke="#3276b5" stroke-width="1.6"><path d="M0 5h12M8 1l4 4-4 4"/></svg></a>
</section>

<section class="about-copy abs">
  <div class="eyebrow">ABOUT</div>
  <h2>BRIGHT HARBOR<span>PROPERTY INSTITUTE</span></h2>
  <h4>OUR STORY</h4>
  <p>Lorem Ipsum is simply dummy text of the printing and typesetting industry. Lorem Ipsum has been the industry's standard dummy text ever since the 1500s, when an unknown printer took a galley of type and scrambled it to make a type specimen book.</p>
  <h4>OUR PROMISE</h4>
  <p>It is a long established fact that a reader will be distracted by the readable content of a page when looking at its layout. The point of using Lorem Ipsum is that it has a more-or-less normal distribution of letters, as opposed to using 'Content here, content here', making it look like readable English. Many desktop publishing packages and web page editors now use Lorem Ipsum as their default model text, and a search for 'lorem ipsum' will uncover many web sites still in their infancy.</p>
</section>
<div class="photo-class abs" role="img" aria-label="Photo of an instructor lecturing to seated adult students"></div>
<div class="photo-laptop abs"><div role="img" aria-label="Blue-toned photo of a student working on a laptop"></div></div>

<div class="city abs" role="img" aria-label="Photo of a city skyline seen from above"></div>
<section class="inquiry abs">
  <h2><b>QUICK</b> INQUIRY</h2>
  <p class="lead">Lorem Ipsum is simply dummy text of the printing and typesetting industry.</p>
  <div class="fields">
    <div class="field">First Name</div><div class="field">Last Name</div><div class="field">Email</div>
    <div class="field">Phone</div><div class="field">Business Name</div><div class="field">Business Type</div>
  </div>
  <a class="submit" href="#">SUBMIT</a>
</section>
<section class="ready abs">
  <h2>READY TO GET STARTED?</h2>
  <a href="#">GET IN TOUCH</a>
</section>

<footer class="footer abs">
  <div class="brand-mark"><span class="dot"></span><span class="name">Bright Harbor<br>Property Institute</span></div>
  <div class="social"><span></span><span></span><span></span><span></span></div>
  <nav class="footer-nav">
    <a href="#">Home</a><a href="#">About Us</a><a href="#">Schedule and Cost</a><a href="#">Registration</a><a href="#">Online Courses</a><a href="#">Our Advantage</a><a href="#">Contact Us</a>
  </nav>
  <p class="copyright">Copyright © 2019 Bright Harbor Property Institute. All Rights Reserved.</p>
</footer>

</body>
</html>
```